create clean, simple business card template

using the logo created now we need to create a simple, elegant business card design to suit

Industry/Entity Type

Business

Font styles to use
Other font styles liked:
• segoe ui

Requirements
Must have
• Front:
"Name:"
"Title:"
"Mobile:"
"email:"
and the logo

Back:
Logo
Nice to have
• Text in black but other graphics etc to match colours in logo as provided

```html
<!DOCTYPE html>
<html lang="en">
<head>
<meta charset="utf-8">
<title>Harlow Property – Business Card</title>
<link rel="stylesheet" href="https://fonts.googleapis.com/css2?family=Open+Sans:wght@400;600;700&display=swap">
<style>
  :root {
    --bg: #e4e4e4;
    --card: #ffffff;
    --gold: #8a7149;
    --gold-soft: #a88d60;
    --dark: #3a322c;
    --ink: #000000;
  }
  * { margin: 0; padding: 0; box-sizing: border-box; }
  html, body {
    width: 1200px; height: 927px; overflow: hidden;
    background: var(--bg);
    font-family: "Open Sans", sans-serif;
  }
  .stage {
    position: relative; width: 1200px; height: 927px;
    display: flex; justify-content: center; align-items: center; gap: 40px;
  }
  .card {
    position: relative; width: 540px; height: 288px;
    background: var(--card); overflow: hidden;
    box-shadow: 0 10px 24px rgba(0,0,0,0.18);
  }
  .brand {
    display: flex; align-items: center; gap: 10px;
    color: var(--gold); font-weight: 600; font-size: 30px; line-height: 1;
  }
  .brand__dot {
    width: 16px; height: 16px; border-radius: 50%; background: var(--dark);
  }
  .card--front .brand { position: absolute; left: 22px; top: 40px; }
  .card--back { display: flex; justify-content: center; align-items: center; }
  .arc { position: absolute; left: 0; top: 0; }
  .roofline {
    position: absolute; left: 0; bottom: 0; width: 320px; height: 104px;
    background: linear-gradient(100deg, var(--gold) 0%, var(--gold-soft) 100%);
  }
  .holder {
    position: absolute; left: 168px; top: 118px; width: 200px;
    text-align: center;
  }
  .holder__name { font-weight: 700; font-size: 33px; color: var(--ink); line-height: 1.1; }
  .holder__title { font-size: 20px; color: var(--ink); line-height: 1.2; }
  .contact {
    position: absolute; right: 22px; bottom: 12px;
    font-size: 16px; color: var(--ink); line-height: 1.6; text-align: right;
  }
</style>
</head>
<body>
  <main class="stage">
    <section class="card card--front" aria-label="Card front">
      <svg class="arc" width="540" height="288" viewBox="0 0 540 288" aria-hidden="true">
        <path d="M505 0 C545 70 540 150 492 216 C518 150 520 70 475 0 Z" fill="var(--dark)"/>
      </svg>
      <div class="brand"><span class="brand__dot"></span>Harlow Property</div>
      <div class="holder">
        <p class="holder__name">Name Here</p>
        <p class="holder__title">Owner</p>
      </div>
      <div class="roofline" role="img" aria-label="Gold house roofline illustration with windows"></div>
      <div class="contact">
        <p>Mobile#: 04123456780</p>
        <p>email: info@hlw.com</p>
      </div>
    </section>
    <section class="card card--back" aria-label="Card back">
      <div class="brand"><span class="brand__dot"></span>Harlow Property</div>
    </section>
  </main>
</body>
</html>
```